Brellick Commercial Roof Restoration LLC needs billboard and banner designs

Need billboard ad design for small commercial roof restoration company. Looking for a billboard design that can be used on digital and hard print billboards. Also need banner design for 4' x 8' job site banners that will go by roadside to draw potential customers to our brand. Our vision for bill board would show an attractive women in business dress, clearly in a building having to use an (red) umbrella (inside building) due to leaking roof. Caption "WE CAN HELP" www.BRELLICKCOMMERCIALROOF.example
For banner design we would use some before/after roof photos (attached, blend/overlay at an angle) in background with "Another Quality Commercial Roof Restoration By:" "Brellick Commercial Roof LLC" "Is your commercial roof leaking? Call 555.318.4726 for help".
All final designs should communicate commercial roof restoration only.
Target Market(s)
Commercial building owner/managers
Industry/Entity Type
Roofing
Font styles to use
Requirements
Must have
- Just added a Jpeg file of a logo of the company that we buy our products from. This logo & "Certified Premier Installers" needs to be added to the project. It only needs to have a small footprint on the ad. Contact me if you have questions. Thank you.
Nice to have
- Billboard design; our name, website, relay our message with image. As described above in project description
Banner; Our name, phone number and bold written message

```html
<!DOCTYPE html>
<html lang="en">
<head>
<meta charset="utf-8">
<title>Brellick Commercial Roof Restoration – Billboard</title>
<link rel="stylesheet" href="https://fonts.googleapis.com/css2?family=Archivo+Black&family=Open+Sans:wght@700;800&display=swap">
<style>
  :root {
    --brand-blue: #0a4f9c;
    --brand-red: #c0261d;
    --paper: #ffffff;
    --stage: #6a6a6a;
    --ceiling: #cdc9c3;
    --wall-warm: #c9b27a;
    --floor-shadow: #8d7a55;
    --umbrella: #e5502f;
  }
  html, body {
    margin: 0;
    padding: 0;
    width: 1200px;
    height: 792px;
    overflow: hidden;
    background: var(--stage);
  }
  .billboard {
    position: absolute;
    left: 0;
    top: 96px;
    width: 1200px;
    height: 600px;
  }
  .billboard svg { display: block; }
  .display-type {
    font-family: "Archivo Black", "Arial Black", sans-serif;
  }
  .url-type {
    font-family: "Open Sans", Arial, sans-serif;
    font-weight: 800;
  }
</style>
</head>
<body>
  <main class="billboard">
    <svg width="1200" height="600" viewBox="0 0 1200 600" xmlns="http://www.w3.org/2000/svg">
      <defs>
        <linearGradient id="scene-tones" x1="0" y1="0" x2="1" y2="0.7">
          <stop offset="0" stop-color="var(--ceiling)"/>
          <stop offset="0.4" stop-color="var(--wall-warm)"/>
          <stop offset="0.7" stop-color="var(--umbrella)"/>
          <stop offset="1" stop-color="var(--floor-shadow)"/>
        </linearGradient>
      </defs>

      <!-- photo panel -->
      <rect class="scene-photo" x="480" y="0" width="720" height="600" fill="url(#scene-tones)"
            role="img" aria-label="Photo: a businesswoman in a light blue coat holding a phone and a red umbrella inside a stairwell lobby, beneath a broken, leaking ceiling"/>

      <!-- red wave band -->
      <path class="wave-red" fill="var(--brand-red)"
            d="M0,0 L640,0 C560,40 498,110 498,192 C498,300 650,420 650,546 C650,570 645,585 636,600 L0,600 Z"/>
      <!-- blue edge line -->
      <path class="wave-blue" fill="var(--brand-blue)"
            d="M0,0 L566,0 C506,32 465,92 465,149 C465,262 611,402 611,527 C611,556 604,581 593,600 L0,600 Z"/>
      <!-- white copy panel -->
      <path class="copy-panel" fill="var(--paper)"
            d="M0,0 L558,0 C500,30 461,90 461,149 C461,260 607,400 607,527 C607,555 600,580 589,600 L0,600 Z"/>

      <!-- company name block -->
      <g class="brand-name display-type">
        <text x="56" y="153" fill="var(--brand-blue)" textLength="320" lengthAdjust="spacingAndGlyphs" font-size="80">BRELLICK</text>
        <text x="56" y="208" fill="var(--brand-blue)" textLength="321" lengthAdjust="spacingAndGlyphs" font-size="44">COMMERCIAL</text>
        <text x="57" y="238" fill="var(--brand-red)" textLength="319" lengthAdjust="spacingAndGlyphs" font-size="27">ROOF RESTORATION</text>
      </g>

      <!-- headline -->
      <path class="headline-band" fill="var(--brand-blue)" d="M62,268 L418,268 L474,347 L62,347 Z"/>
      <text class="headline-top display-type" x="102" y="335" fill="var(--paper)"
            font-size="70" textLength="288" lengthAdjust="spacingAndGlyphs">WE CAN</text>
      <text class="headline-main display-type" x="60" y="484" fill="var(--brand-red)"
            font-size="170" textLength="451" lengthAdjust="spacingAndGlyphs">HELP</text>

      <!-- website bar -->
      <path class="url-bar" fill="var(--brand-blue)"
            d="M62,512 L511,512 Q519,512 519,520 L519,552 Q519,560 511,560 L62,560 Z"/>
      <text class="url-type" x="93" y="545" fill="var(--paper)" font-size="24"
            textLength="397" lengthAdjust="spacingAndGlyphs">www.BRELLICKCOMMERCIALROOF.example</text>
    </svg>
  </main>
</body>
</html>
```